Corvell Upholstery & Design
Stationary & Biz Card
Project: Corvell Upholstery & Design
Corvell Upholstery & Design -
Creative Brief
Bright & Fun-filled
Dorin Velasq
Owner
51847 Pellinore Court Sterling, VA 20166
dorin@corvellupholstery-example.com
www.corvellupholstery-example.com

```html
<!DOCTYPE html>
<html lang="en">
<head>
<meta charset="utf-8">
<title>Corvell Upholstery &amp; Design – Stationery</title>
<link href="https://fonts.googleapis.com/css2?family=Montserrat:wght@300;400&display=swap" rel="stylesheet">
<style>
:root{
  --board:#2f2f31;
  --paper:#ffffff;
  --art-tone:#efefef;
  --art-tone-light:#f8f8f8;
  --brand-red:#d9363e;
  --ink:#8a8a8a;
  --label:#9a9a9a;
  --envelope-grey:#7c7c80;
  --envelope-grey-dark:#5d5d61;
}
*{box-sizing:border-box;margin:0;padding:0}
html,body{width:1200px;height:312px;overflow:hidden;background:var(--board)}
body{font-family:"Montserrat",sans-serif;position:relative}
.piece{position:absolute;background:var(--paper);box-shadow:0 2px 6px rgba(0,0,0,.45);overflow:hidden}
.label{position:absolute;font-size:4px;color:var(--label);letter-spacing:.2px;white-space:nowrap}
.brand{display:flex;flex-direction:column;align-items:center;color:var(--brand-red);font-weight:300}
.brand-dot{width:7px;height:7px;border-radius:50%;border:1px solid currentColor;margin-bottom:2px}
.brand-name{font-size:9px;letter-spacing:3px;line-height:1}
.brand-tag{font-size:3px;letter-spacing:.8px;color:var(--ink);margin-top:2px;white-space:nowrap}
.contact{font-size:3px;line-height:4.6px;color:var(--ink);white-space:nowrap}

/* neutral placeholder for the faint decorative illustration */
.art-area{position:absolute;background:linear-gradient(180deg,var(--art-tone-light),var(--art-tone))}

/* business cards */
.card{width:82px;height:48px}
.card .brand{position:absolute;left:0;right:0;top:12px}
.card .brand-name{font-size:7px;letter-spacing:2px}
.card--red{background:var(--brand-red)}
.card--red .brand,.card--red .brand-tag{color:var(--paper)}
.card--info .brand{top:6px;left:auto;right:6px;align-items:flex-end}
.card--info .brand-name{font-size:5px}
.card--info .contact{position:absolute;left:6px;bottom:6px}

/* letterheads */
.letterhead{width:209px;height:272px;top:19px}
.letterhead .brand{position:absolute;left:0;right:0;top:12px}
.letterhead .art-area{left:60px;top:82px;width:89px;height:139px}
.letterhead .contact{position:absolute;bottom:12px;left:0;right:0;text-align:center}
.letterhead--side .contact{text-align:left;left:12px}

/* envelope fronts */
.envelope{width:223px;height:103px;left:672px}
.envelope .brand{position:absolute;left:10px;top:9px;align-items:flex-start}
.envelope .brand-name{font-size:6px;letter-spacing:2px}
.envelope .contact{position:absolute;left:10px;top:28px}
.envelope .art-area{left:160px;top:22px;width:44px;height:62px}

/* large envelope set */
.env-back{width:264px;left:912px;background:var(--envelope-grey)}
.env-back svg{position:absolute;inset:0}
.env-back .brand{position:absolute;left:0;right:0;top:8px;color:var(--paper)}
.env-front{width:264px;height:108px;left:912px;top:150px}
.env-front .brand{position:absolute;left:0;right:0;top:34px}
.env-front .contact{position:absolute;right:10px;bottom:8px;text-align:right}
</style>
</head>
<body>

<!-- business cards -->
<div class="piece card" style="left:24px;top:104px">
  <div class="brand"><span class="brand-dot"></span><span class="brand-name">CORVELL</span><span class="brand-tag">UPHOLSTERY &amp; DESIGN</span></div>
</div>
<span class="label" style="left:24px;top:155px">Business Card Front</span>

<div class="piece card card--info" style="left:115px;top:104px">
  <div class="brand"><span class="brand-name">CORVELL</span></div>
  <div class="contact">Dorin Velasq · Owner<br>dorin@corvellupholstery-example.com<br>www.corvellupholstery-example.com</div>
</div>
<span class="label" style="left:115px;top:155px">Business Card Back</span>

<div class="piece card" style="left:24px;top:172px">
  <div class="brand"><span class="brand-dot"></span><span class="brand-name">CORVELL</span><span class="brand-tag">UPHOLSTERY &amp; DESIGN</span></div>
</div>
<span class="label" style="left:24px;top:223px">Business Card Front</span>

<div class="piece card card--red" style="left:115px;top:172px">
  <div class="brand"><span class="brand-dot"></span><span class="brand-name">CORVELL</span><span class="brand-tag">UPHOLSTERY &amp; DESIGN</span></div>
</div>
<span class="label" style="left:115px;top:223px">Business Card Back</span>

<!-- letterheads -->
<div class="piece letterhead letterhead--side" style="left:223px">
  <div class="brand"><span class="brand-dot"></span><span class="brand-name">CORVELL</span><span class="brand-tag">UPHOLSTERY &amp; DESIGN</span></div>
  <div class="art-area" role="img" aria-label="Area for a faint upholstered chair illustration"></div>
  <div class="contact">Dorin Velasq<br>51847 Pellinore Court Sterling, VA 20166<br>dorin@corvellupholstery-example.com<br>www.corvellupholstery-example.com</div>
</div>
<span class="label" style="left:330px;top:295px">Letterhead Front</span>

<div class="piece letterhead" style="left:444px">
  <div class="brand"><span class="brand-dot"></span><span class="brand-name">CORVELL</span><span class="brand-tag">UPHOLSTERY &amp; DESIGN</span></div>
  <div class="art-area" role="img" aria-label="Area for a faint upholstered chair illustration"></div>
  <div class="contact">51847 Pellinore Court Sterling, VA 20166<br>dorin@corvellupholstery-example.com · www.corvellupholstery-example.com</div>
</div>
<span class="label" style="left:551px;top:295px">Letterhead Back</span>

<!-- envelope fronts -->
<div class="piece envelope" style="top:34px">
  <div class="brand"><span class="brand-name">CORVELL</span><span class="brand-tag">UPHOLSTERY &amp; DESIGN</span></div>
  <div class="contact">51847 Pellinore Court<br>Sterling, VA 20166</div>
  <div class="art-area" role="img" aria-label="Area for a faint upholstered chair illustration"></div>
</div>
<span class="label" style="left:840px;top:140px">Envelope Front</span>

<div class="piece envelope" style="top:158px">
  <div class="brand"><span class="brand-name">CORVELL</span><span class="brand-tag">UPHOLSTERY &amp; DESIGN</span></div>
  <div class="contact">51847 Pellinore Court<br>Sterling, VA 20166</div>
  <div class="art-area" role="img" aria-label="Area for a faint upholstered chair illustration"></div>
</div>
<span class="label" style="left:840px;top:264px">Envelope Front</span>

<!-- large envelope: flaps and front -->
<div class="piece env-back" style="top:19px;height:66px">
  <svg width="264" height="66" viewBox="0 0 264 66"><path d="M0 0 L132 46 L264 0 Z" fill="var(--envelope-grey-dark)"/></svg>
  <div class="brand"><span class="brand-dot"></span><span class="brand-name">CORVELL</span></div>
</div>
<div class="piece env-back" style="top:86px;height:60px">
  <svg width="264" height="60" viewBox="0 0 264 60"><path d="M0 0 L132 42 L264 0 Z" fill="var(--envelope-grey-dark)"/></svg>
</div>

<div class="piece env-front">
  <div class="brand"><span class="brand-dot"></span><span class="brand-name">CORVELL</span><span class="brand-tag">UPHOLSTERY &amp; DESIGN</span></div>
  <div class="contact">www.corvellupholstery-example.com</div>
</div>
<span class="label" style="left:1030px;top:263px">Envelope Back</span>

</body>
</html>
```